New Television Homescreen Template

We need a new default homescreen design for our televisions. This should reflect our company branding. My company is called Wellward Systems, WSY for short. Our website is www.wsyq.com. We develop televisions and infotainment solutions for the healthcare industry. I am somewhat open to different color palettes but our company colors are blue, black, and white. Our design is constrained by the 9 buttons, however the design of the buttons can be changed. Also, there is a video box on the right side of the screen as shown, this design can also be changed.

Target Market(s)

Hospital Patients

Requirements
Must have
• PSD template.

```html
<!DOCTYPE html>
<html lang="en">
<head>
<meta charset="utf-8">
<title>Wellward Systems – Homescreen</title>
<link rel="stylesheet" href="https://fonts.googleapis.com/css2?family=Open+Sans:wght@400;600&family=Dosis:wght@300;400&display=swap">
<style>
  :root {
    --black: #000000;
    --deep: #031521;
    --panel: #0b2434;
    --tile: #143246;
    --tile-edge: #2c4c60;
    --label: #0d2130;
    --band: #1587b8;
    --white: #ffffff;
    --ink-soft: #d9e6ee;
    --grey-title: #8e9ba5;
    --brand-blue: #3db4e5;
    --screen: #4a4a4a;
    --play-bg: #c7d0d6;
    --play-arrow: #1577b3;
  }
  html, body { margin: 0; padding: 0; overflow: hidden; }
  body { width: 1200px; height: 747px; background: var(--black); }
  .homescreen {
    position: relative; width: 1200px; height: 747px; overflow: hidden;
    font-family: "Open Sans", Arial, sans-serif;
    background: linear-gradient(180deg, #0a2a3e 117px, #0d3b56 300px, #0f4f72 560px, var(--deep) 585px);
  }
  .topbar { position: absolute; left: 0; top: 0; width: 1200px; height: 117px; background: var(--black); }
  .brand {
    position: absolute; left: 0; top: 0; width: 1200px; height: 117px;
    display: flex; align-items: center; justify-content: center; gap: 12px;
  }
  .brand-square { width: 22px; height: 22px; background: var(--brand-blue); }
  .brand-name { color: var(--white); font-size: 38px; font-weight: 400; line-height: 1; letter-spacing: -0.5px; }

  .glow { position: absolute; border-radius: 50%; background: rgba(255,255,255,0.05); }
  .glow.small { left: 718px; top: 120px; width: 160px; height: 160px; }
  .glow.large { left: 790px; top: 60px; width: 350px; height: 350px; background: rgba(255,255,255,0.035); }

  .menu { position: absolute; left: 0; top: 0; }
  .tile {
    position: absolute; width: 112px; height: 124px;
    background: linear-gradient(180deg, #1a3c52, var(--tile));
    border: 1px solid var(--tile-edge); box-shadow: 0 2px 6px rgba(0,0,0,0.5);
  }
  .tile-icon { position: absolute; left: 24px; top: 6px; width: 64px; height: 64px; border-radius: 12px; }
  .tile-label {
    position: absolute; left: 44px; top: 74px; width: 88px; height: 40px;
    background: var(--label); color: var(--ink-soft); font-size: 19px;
    display: flex; align-items: center; justify-content: center;
    box-shadow: 0 1px 3px rgba(0,0,0,0.6);
  }
  .icon-blue { background: radial-gradient(circle at 40% 35%, #5fb0ef, #13499b); border-radius: 50%; }
  .icon-gold { background: linear-gradient(180deg, #ffd23a, #e08e00); }
  .icon-grey { background: linear-gradient(180deg, #9a9a9a, #3d3d3d); }
  .icon-dark { background: linear-gradient(180deg, #4a4a4a, #0c0c0c); }
  .icon-cap { background: linear-gradient(180deg, #2a2a2a, #e8dcc0); }
  .icon-chat { background: radial-gradient(circle at 45% 45%, #e6f4fb, #8fc7e6); border-radius: 50%; }

  .intro { position: absolute; left: 793px; top: 152px; }
  .intro-kicker { font-family: "Dosis", sans-serif; font-weight: 300; font-size: 46px; letter-spacing: 2px; color: var(--grey-title); line-height: 1; }
  .intro-product { margin-top: 6px; font-family: "Dosis", sans-serif; font-weight: 400; font-size: 28px; color: var(--ink-soft); line-height: 36px; }

  .video { position: absolute; left: 745px; top: 308px; width: 437px; height: 260px; background: var(--panel); border-radius: 4px; box-shadow: 0 0 6px rgba(0,0,0,0.5); }
  .video-screen { position: absolute; left: 17px; top: 14px; width: 404px; height: 188px; background: var(--screen); border-radius: 3px; }
  .video-thumb { position: absolute; left: 28px; top: 20px; width: 130px; height: 155px; background: radial-gradient(circle, #2f5866, var(--screen) 70%); }
  .play { position: absolute; left: 178px; top: 74px; width: 46px; height: 33px; }
  .progress { position: absolute; left: 20px; top: 224px; width: 403px; height: 4px; background: #2a4656; }
  .progress-knob { position: absolute; left: 30px; top: -4px; width: 4px; height: 12px; background: #d4dde2; }

  .footer-band { position: absolute; left: 0; top: 585px; width: 1200px; height: 162px; background: linear-gradient(180deg, var(--band), #0b4a6c 40%, var(--deep)); }
  .footer-line { position: absolute; left: 255px; top: 646px; margin: 0; color: var(--ink-soft); font-size: 21.5px; white-space: nowrap; }
</style>
</head>
<body>
<main class="homescreen">
  <header class="topbar">
    <div class="brand"><span class="brand-square"></span><span class="brand-name">Wellward Systems</span></div>
  </header>

  <div class="glow large"></div>
  <div class="glow small"></div>

  <nav class="menu">
    <div class="tile" style="left:93px;top:148px"><div class="tile-icon icon-blue" role="img" aria-label="Television icon"></div><div class="tile-label">TV</div></div>
    <div class="tile" style="left:330px;top:148px"><div class="tile-icon icon-gold" role="img" aria-label="Photo gallery folder icon"></div><div class="tile-label">Gallery</div></div>
    <div class="tile" style="left:565px;top:148px"><div class="tile-icon icon-grey" role="img" aria-label="Games folder icon"></div><div class="tile-label">Games</div></div>
    <div class="tile" style="left:95px;top:302px"><div class="tile-icon icon-blue" role="img" aria-label="Information icon"></div><div class="tile-label">info</div></div>
    <div class="tile" style="left:332px;top:302px"><div class="tile-icon icon-dark" role="img" aria-label="Movies folder icon"></div><div class="tile-label">Movies</div></div>
    <div class="tile" style="left:566px;top:302px"><div class="tile-icon icon-dark" role="img" aria-label="Folder icon"></div><div class="tile-label">Folder</div></div>
    <div class="tile" style="left:96px;top:450px"><div class="tile-icon icon-cap" role="img" aria-label="Graduation cap and diploma icon"></div><div class="tile-label">Education</div></div>
    <div class="tile" style="left:332px;top:450px"><div class="tile-icon icon-blue" role="img" aria-label="Globe icon"></div><div class="tile-label">Web</div></div>
    <div class="tile" style="left:566px;top:450px"><div class="tile-icon icon-chat" role="img" aria-label="Chat bubble with pencil icon"></div><div class="tile-label">Chat</div></div>
  </nav>

  <section class="intro">
    <div class="intro-kicker">INTRODUCING</div>
    <div class="intro-product">Cotrest 15″ Orbitra<br>Touchscreen</div>
  </section>

  <section class="video">
    <div class="video-screen">
      <div class="video-thumb" role="img" aria-label="Stethoscope video thumbnail"></div>
      <svg class="play" viewBox="0 0 46 33" aria-label="Play">
        <rect width="46" height="33" rx="3" fill="var(--play-bg)"/>
        <polygon points="17,8 32,16.5 17,25" fill="var(--play-arrow)"/>
      </svg>
    </div>
    <div class="progress"><div class="progress-knob"></div></div>
  </section>

  <footer class="footer-band"></footer>
  <p class="footer-line">The best of a tablet,&nbsp; TV fused together that is perfect&nbsp; care facility.</p>
</main>
</body>
</html>
```